Velvet Monsoon 2 EP - Album Cover ARTwork

I need an album cover ARTWORK for my new digital EP. Emphasis on the word ART ! It has to be artistic,creative & inspiring.NOT marketing stuff.It has to be minimal & clean.I make TRIBAL music which combines primitive\primal\ancient rhythms with new techy electronica.Listen here : https://tunewharf.example/kelpordaudio
kelpordaudio.example

Cover must include :
1.Title : Velvet Monsoon 2 EP
2.My logo ( attached )

Use your imagination,inspiration & design mastery to visualize VELVET MONSOON !

Digital Music

Digital

Must have
• 1.Title : Velvet Monsoon 2 EP
• 2.My logo ( attached )

```html
<!DOCTYPE html>
<html lang="en">
<head>
<meta charset="utf-8">
<title>Velvet Monsoon 2 EP — Cover</title>
<link rel="stylesheet" href="https://fonts.googleapis.com/css2?family=Orbitron:wght@500&display=swap">
<style>
  :root {
    --ink: #08070b;
    --panel: #0c1416;
    --night: #1a1a2e;
    --sea: #2aa6c4;
    --sun: #c9d23c;
    --ember: #f0522a;
    --dusk: #3a2a5e;
    --wordmark: #d8352a;
    --silver: #c9ccd2;
  }
  html, body {
    margin: 0;
    padding: 0;
    overflow: hidden;
    background: var(--ink);
  }
  .cover {
    position: relative;
    width: 1200px;
    height: 1200px;
    background: var(--ink);
    overflow: hidden;
  }
  .cover-art {
    position: absolute;
    inset: 0;
    width: 1200px;
    height: 1200px;
  }
  .release-title {
    position: absolute;
    left: 0;
    right: 0;
    top: 48px;
    margin: 0;
    text-align: center;
    font-family: "Orbitron", sans-serif;
    font-weight: 500;
    font-size: 34px;
    line-height: 44px;
    letter-spacing: 10px;
    color: var(--silver);
  }
  .artist-name {
    position: absolute;
    left: 0;
    right: 0;
    top: 1000px;
    margin: 0;
    text-align: center;
    font-family: "Orbitron", sans-serif;
    font-weight: 500;
    font-size: 128px;
    line-height: 140px;
    letter-spacing: 4px;
    color: var(--wordmark);
  }
</style>
</head>
<body>
  <main class="cover">
    <svg class="cover-art" viewBox="0 0 1200 1200" xmlns="http://www.w3.org/2000/svg">
      <defs>
        <linearGradient id="triangle-scene" x1="0" y1="0" x2="0" y2="1">
          <stop offset="0" stop-color="var(--night)"/>
          <stop offset="0.25" stop-color="var(--night)"/>
          <stop offset="0.3" stop-color="var(--sea)"/>
          <stop offset="0.5" stop-color="var(--sun)"/>
          <stop offset="0.68" stop-color="var(--ember)"/>
          <stop offset="0.82" stop-color="var(--dusk)"/>
          <stop offset="1" stop-color="#5a1030"/>
        </linearGradient>
      </defs>
      <rect class="textured-backdrop" x="24" y="0" width="1152" height="1008" fill="var(--panel)"
            role="img" aria-label="Dark flowing line texture with silhouettes of birds"/>
      <polygon class="triangle-scene" points="128,140 1072,140 604,916" fill="url(#triangle-scene)"
               role="img" aria-label="Inverted triangle: starry night sky, a patterned moon, and a mirrored psychedelic landscape with a lone figure walking"/>
    </svg>
    <h1 class="release-title">VELVET MONSOON 2 EP</h1>
    <p class="artist-name">KELPORD</p>
  </main>
</body>
</html>
```